Tutoring Site Hero Image Design

Updated Hero Concept for BrightlaneLessons.com

Create a hero that communicates “high quality, in-person private tutoring for all ages,” with warmth, credibility, and a real-life feel. The hero should move away from generic stock photography and better reflect the moments that make our service different: tutors meeting students where they are, one-on-one engagement, and a range of ages.

What the New Hero Should Convey
1. In-person, private, one-on-one support
This is the core differentiator, so the visual should feel intimate, focused, and real. Avoid anything that resembles online learning settings or learning-center classrooms.

2. Coverage of age ranges without clutter
We serve elementary through college. We do not need multiple students in the hero, but the chosen student should not skew strongly to one age group. Aim for a middle-ground age that feels inclusive, for example a middle schooler or early high schooler.

3. Realistic, authentic moments
Use photography that feels candid and warm. Natural light, home settings, kitchen tables, quiet study nooks, or library corners work well. Avoid staged stock looks, harsh lighting, or exaggerated classroom setups.

Design the hero at 2400 × 1200 px, with the focal point on the right side, safe area leaving room on the left for a stacked headline and form.

Images that I've shared as just thought starters and do not need to be used in the design.

Font styles to use
Sans Serif

Colors
0054AA
0677BA
7BADD7
CADEEF
E8F1F8
EB3D1F
EC4F4E
F09395
F8D3D4
FCEDEE
6B429C
8869AF
B7A5CE
E3DAEB
F3F0F8

```html
<!DOCTYPE html>
<html lang="en">
<head>
<meta charset="utf-8">
<title>BrightlaneLessons.com — One-on-one tutoring hero</title>
<link rel="stylesheet" href="https://fonts.googleapis.com/css2?family=Roboto+Condensed:wght@700&family=Montserrat:wght@400&family=Roboto:wght@400&display=swap">
<style>
  :root {
    --deep-red: #6a0020;
    --plum: #45105e;
    --indigo: #24237f;
    --navy: #0b2c6f;
    --blue: #0054AA;
    --blue-bright: #0677BA;
    --red: #EB3D1F;
    --purple: #6B429C;
    --lavender: #E3DAEB;
    --lavender-soft: #F3F0F8;
    --white: #ffffff;
    --ink: #1b1b24;
  }
  * { margin: 0; padding: 0; box-sizing: border-box; }
  html, body { width: 1200px; height: 627px; overflow: hidden; background: var(--lavender-soft); }
  .hero {
    position: relative;
    width: 1200px;
    height: 627px;
    overflow: hidden;
    background: linear-gradient(90deg, var(--deep-red) 0%, var(--plum) 22%, var(--indigo) 50%, var(--navy) 100%);
  }
  .hero-art { position: absolute; inset: 0; width: 1200px; height: 627px; }
  .hero-copy {
    position: absolute;
    left: 90px;
    top: 132px;
    width: 520px;
    color: var(--white);
  }
  .hero-headline {
    font-family: "Roboto Condensed", "Arial Narrow", sans-serif;
    font-weight: 700;
    font-size: 46px;
    line-height: 54px;
    letter-spacing: -0.2px;
  }
  .hero-subhead {
    margin-top: 14px;
    font-family: "Montserrat", Arial, sans-serif;
    font-weight: 400;
    font-size: 19.5px;
    line-height: 25px;
  }
  .hero-actions {
    display: flex;
    gap: 24px;
    margin-top: 28px;
  }
  .btn {
    display: inline-flex;
    align-items: center;
    justify-content: center;
    height: 40px;
    border-radius: 6px;
    text-decoration: none;
  }
  .btn-outline {
    width: 148px;
    border: 1.5px solid var(--white);
    color: var(--white);
    font-family: "Roboto Condensed", "Arial Narrow", sans-serif;
    font-weight: 700;
    font-size: 23px;
  }
  .btn-solid {
    width: 238px;
    height: 42px;
    margin-top: -1px;
    background: var(--lavender);
    color: var(--ink);
    font-family: "Roboto", Arial, sans-serif;
    font-size: 21px;
    box-shadow: 0 2px 6px rgba(0,0,0,0.25);
  }
</style>
</head>
<body>
<main class="hero">
  <svg class="hero-art" viewBox="0 0 1200 627" xmlns="http://www.w3.org/2000/svg">
    <defs>
      <radialGradient id="photoTone" cx="0.45" cy="0.35" r="0.75">
        <stop offset="0" stop-color="#efe2c8"/>
        <stop offset="0.45" stop-color="#b59a7e"/>
        <stop offset="0.75" stop-color="#2f6e86"/>
        <stop offset="1" stop-color="#2a5a9a"/>
      </radialGradient>
      <linearGradient id="stripeGlow" x1="0" y1="1" x2="1" y2="0">
        <stop offset="0" stop-color="#ff9ad0" stop-opacity="0.45"/>
        <stop offset="1" stop-color="#b07cff" stop-opacity="0"/>
      </linearGradient>
    </defs>

    <g class="stripes-lower-left">
      <polygon points="0,560 170,390 190,390 20,560" fill="#ff8fb0" opacity="0.25"/>
      <polygon points="40,627 300,367 340,367 80,627" fill="url(#stripeGlow)"/>
      <polygon points="110,627 360,377 395,377 145,627" fill="url(#stripeGlow)" opacity="0.8"/>
      <polygon points="190,627 430,387 500,387 260,627" fill="url(#stripeGlow)" opacity="0.7"/>
      <polygon points="290,627 520,397 560,397 330,627" fill="url(#stripeGlow)" opacity="0.5"/>
      <polygon points="380,627 600,407 630,407 410,627" fill="url(#stripeGlow)" opacity="0.35"/>
    </g>

    <g class="stripes-upper-right" fill="#1f6fd0" opacity="0.5">
      <polygon points="1010,0 1040,0 960,80 930,80"/>
      <polygon points="1060,0 1110,0 1000,110 950,110"/>
      <polygon points="1140,0 1200,0 1200,20 1090,130 1040,130"/>
      <polygon points="1200,60 1200,110 1110,200 1080,180"/>
      <polygon points="1200,140 1200,180 1120,260 1110,230"/>
    </g>

    <path class="arc-blue" d="M745 58 A300 300 0 0 1 1162 300 A285 285 0 0 0 752 64 Z" fill="var(--blue)"/>
    <path class="arc-red" d="M618 350 A270 270 0 0 1 1050 112 A258 258 0 0 0 626 335 Z" fill="var(--red)"/>
    <path class="arc-lavender" d="M745 128 A262 262 0 0 0 912 598 A250 250 0 0 1 760 138 Z" fill="var(--lavender)"/>

    <g role="img" aria-label="Photo: a tutor and a young teen student working together over notebooks at a table in a warm, naturally lit home">
      <circle cx="915" cy="310" r="247" fill="url(#photoTone)"/>
    </g>

    <path class="arc-purple" d="M694 414 A262 262 0 0 0 1172 430 A250 248 0 0 1 702 422 Z" fill="var(--purple)"/>
  </svg>

  <section class="hero-copy">
    <h1 class="hero-headline">One-on-one<br>support for every grade<br>from elementary to college.</h1>
    <p class="hero-subhead">Connecting students with experienced,<br>one-on-one tutors for personalized support<br>from elementary to college.</p>
    <div class="hero-actions">
      <a class="btn btn-outline" href="#">Get Started</a>
      <a class="btn btn-solid" href="#">Call (555) 014-2387</a>
    </div>
  </section>
</main>
</body>
</html>
```